Colin Dwyer Moving DL Flyer

We need a double sided DL flyer to give to patients to let them know that we are moving location.
On one side we would like it to read:
"We Are Moving!" and "November 2017" and our logo.
On the other side we would like it to read:
"Same Great Staff"
"Same Great Service"
"Bigger, Brighter and Better"
"New Location at 52 Fernlow St"
with a map below (attached)
The flyer should follow our practice branding. Attached is a copy of our business card as an example of this.

```html
<!DOCTYPE html>
<html lang="en">
<head>
<meta charset="utf-8">
<title>Colin Dwyer Optometry – Moving DL Flyer</title>
<link href="https://fonts.googleapis.com/css2?family=Roboto:wght@300;400&display=swap" rel="stylesheet">
<style>
  :root {
    --backdrop: #ece9e4;
    --paper: #ffffff;
    --paper-shade: #e4e4e6;
    --plum: #4b3a55;
    --plum-text: #5a4a63;
    --red: #d0171d;
    --white: #ffffff;
    --cart-brown: #b98a5c;
    --cart-red: #d8332f;
    --map-grey: #c9c9cb;
    --map-road: #2b2b2b;
  }
  * { box-sizing: border-box; margin: 0; padding: 0; }
  html, body { width: 1200px; height: 889px; overflow: hidden; }
  body {
    background: var(--backdrop);
    font-family: "Roboto", Arial, sans-serif;
    position: relative;
  }

  /* Front side */
  .flyer-front {
    position: absolute;
    left: 110px; top: 300px;
    width: 620px; height: 300px;
    background: linear-gradient(180deg, var(--paper) 0%, var(--paper-shade) 100%);
    box-shadow: 0 4px 14px rgba(0,0,0,.18);
  }
  .front-illustration {
    position: absolute;
    left: 40px; top: 70px;
    width: 190px; height: 190px;
    background: linear-gradient(160deg, var(--cart-brown) 0%, #9c7048 70%, var(--cart-red) 100%);
    border-radius: 4px;
  }
  .front-copy {
    position: absolute;
    left: 250px; top: 50px;
    width: 340px;
    text-align: center;
  }
  .moving-headline {
    font-weight: 300;
    font-size: 27px;
    color: var(--plum-text);
  }
  .moving-date {
    font-weight: 400;
    font-size: 42px;
    color: var(--red);
    margin-top: 2px;
    line-height: 1.05;
  }
  .date-rule {
    width: 310px; height: 5px;
    background: var(--plum);
    margin: 8px auto 0;
  }
  .practice-name {
    display: inline-flex;
    align-items: center;
    gap: 10px;
    margin-top: 44px;
    font-weight: 400;
    font-size: 24px;
    color: var(--plum);
  }
  .practice-name .mark {
    width: 14px; height: 14px;
    background: var(--plum);
  }

  /* Back side */
  .flyer-back {
    position: absolute;
    left: 790px; top: 145px;
    width: 290px; height: 590px;
    background: var(--paper);
    box-shadow: 0 4px 14px rgba(0,0,0,.18);
    overflow: hidden;
  }
  .back-banner {
    height: 300px;
    background: var(--plum);
    color: var(--white);
    text-align: center;
    padding-top: 22px;
  }
  .promise-line {
    font-weight: 300;
    font-size: 11.5px;
  }
  .banner-rule {
    width: 236px; height: 2px;
    background: var(--white);
    margin: 0 auto;
  }
  .banner-rule.top { margin-top: 28px; }
  .headline {
    font-weight: 400;
    font-size: 27px;
    line-height: 1.25;
    padding: 10px 0 8px;
  }
  .location-label {
    font-weight: 300;
    font-size: 14px;
    margin-top: 24px;
  }
  .address-box {
    display: inline-block;
    margin-top: 14px;
    border: 2px solid var(--white);
    padding: 8px 16px;
    font-size: 21px;
    font-weight: 400;
  }
  .pointer {
    display: block;
    margin: 6px auto 0;
  }
  .location-map {
    position: absolute;
    left: 36px; top: 328px;
    width: 218px; height: 228px;
    background: radial-gradient(circle at 60% 50%, #d99090 0%, var(--map-grey) 45%, var(--map-road) 100%);
  }
</style>
</head>
<body>

  <section class="flyer-front" aria-label="Flyer front">
    <div class="front-illustration" role="img" aria-label="Illustration of a red hand truck carrying two cardboard moving boxes"></div>
    <div class="front-copy">
      <p class="moving-headline">We Are Moving!</p>
      <p class="moving-date">November 2017</p>
      <div class="date-rule"></div>
      <p class="practice-name"><span class="mark"></span>Colin Dwyer Optometry</p>
    </div>
  </section>

  <section class="flyer-back" aria-label="Flyer back">
    <div class="back-banner">
      <p class="promise-line">Same Great Staff&nbsp; | &nbsp;Same Great Service</p>
      <div class="banner-rule top"></div>
      <h1 class="headline">Bigger, Brighter<br>and Better</h1>
      <div class="banner-rule"></div>
      <p class="location-label">New Location at</p>
      <p class="address-box">52 Fernlow St</p>
    </div>
    <svg class="pointer" width="20" height="34" viewBox="0 0 20 34" style="position:absolute;left:135px;top:270px" aria-hidden="true">
      <rect x="8" y="0" width="4" height="20" fill="#ffffff"/>
      <polygon points="2,18 18,18 10,32" fill="#ffffff"/>
    </svg>
    <div class="location-map" role="img" aria-label="Street map showing the new practice location beside the marketplace"></div>
  </section>

</body>
</html>
```